Business Cards for a law firm

Business cards for our law firm. Use our silhoette logo and OAK COUNSEL - check our website (www.oakcounsel.com)

Contact Information for Business Card

our silhouette logo, OAK COUNSEL, 800-555-0147, Dariel Montague, dariel@oakcounsel.com

Requirements
Must have
• our silhouette logo, OAK COUNSEL, 800-555-0147, Dariel Montague, dariel@oakcounsel.com

```html
<!DOCTYPE html>
<html lang="en">
<head>
<meta charset="utf-8">
<title>Oak Counsel — Business Cards</title>
<link href="https://fonts.googleapis.com/css2?family=Cinzel:wght@600&family=Arimo:wght@400&display=swap" rel="stylesheet">
<style>
  :root {
    --backdrop: #3b3b3b;
    --card-dark: #333333;
    --paper: #ffffff;
    --navy: #1e3270;
    --ink-grey: #555555;
    --light: #ffffff;
  }
  * { margin: 0; padding: 0; box-sizing: border-box; }
  html, body { width: 1200px; height: 689px; overflow: hidden; }
  body { background: var(--backdrop); position: relative; }

  .card {
    position: absolute;
    top: 196px;
    width: 520px;
    height: 297px;
    border-radius: 14px;
    overflow: hidden;
  }
  .card--back { left: 50px; background: var(--card-dark); }
  .card--front { left: 630px; background: var(--card-dark); }

  .card__shapes { position: absolute; inset: 0; }

  /* Back */
  .back__mark {
    position: absolute;
    left: 0; right: 0; top: 108px;
    text-align: center;
    font-family: "Cinzel", serif;
    font-weight: 600;
    font-size: 30px;
    letter-spacing: 2px;
    color: var(--light);
  }
  .back__url {
    position: absolute;
    left: 0; right: 0; top: 200px;
    text-align: center;
    font-family: "Arimo", sans-serif;
    font-size: 13px;
    color: var(--light);
  }

  /* Front */
  .brand {
    position: absolute;
    left: 30px; top: 100px;
    display: flex; align-items: center; gap: 10px;
  }
  .brand__dot { width: 22px; height: 22px; border-radius: 50%; background: var(--navy); }
  .brand__name {
    font-family: "Cinzel", serif;
    font-weight: 600;
    font-size: 26px;
    letter-spacing: 1.5px;
    color: var(--navy);
  }
  .person {
    position: absolute;
    left: 30px; top: 178px;
    font-family: "Cinzel", serif;
    font-weight: 600;
    font-size: 18px;
    letter-spacing: 1px;
    color: var(--navy);
  }
  .contact {
    position: absolute;
    left: 30px; top: 212px;
    list-style: none;
    font-family: "Arimo", sans-serif;
    font-size: 12.5px;
    color: var(--ink-grey);
  }
  .contact li { display: flex; align-items: center; gap: 8px; height: 19px; }
  .contact svg { width: 11px; height: 11px; fill: var(--navy); }
</style>
</head>
<body>

  <section class="card card--back" aria-label="Card back">
    <div class="back__mark">OAK COUNSEL</div>
    <div class="back__url">www.oakcounsel.com</div>
  </section>

  <section class="card card--front" aria-label="Card front">
    <svg class="card__shapes" viewBox="0 0 520 297" preserveAspectRatio="none" aria-hidden="true">
      <path d="M412 0 C480 40 515 120 520 210 V297 H470 C490 170 470 70 395 6 Z" fill="var(--navy)"/>
      <path d="M0 0 H360 C445 30 475 150 450 297 H0 Z" fill="var(--paper)"/>
      <path d="M385 4 C470 40 505 130 505 200" fill="none" stroke="var(--paper)" stroke-width="3"/>
    </svg>

    <div class="brand">
      <span class="brand__dot"></span>
      <span class="brand__name">OAK COUNSEL</span>
    </div>

    <div class="person">Dariel Montague</div>

    <ul class="contact">
      <li>
        <svg viewBox="0 0 24 24"><path d="M6.6 10.8a15 15 0 0 0 6.6 6.6l2.2-2.2a1 1 0 0 1 1-.25 11.4 11.4 0 0 0 3.6.57 1 1 0 0 1 1 1V20a1 1 0 0 1-1 1A17 17 0 0 1 3 4a1 1 0 0 1 1-1h3.5a1 1 0 0 1 1 1c0 1.25.2 2.45.57 3.57a1 1 0 0 1-.25 1z"/></svg>
        800-555-0147
      </li>
      <li>
        <svg viewBox="0 0 24 24"><path d="M2 5h20v14H2z M2 5l10 8 10-8" fill="none" stroke="var(--navy)" stroke-width="2.5"/></svg>
        dariel@oakcounsel.com
      </li>
      <li>
        <svg viewBox="0 0 24 24"><circle cx="12" cy="12" r="10"/></svg>
        www.oakcounsel.com
      </li>
    </ul>
  </section>

</body>
</html>
```